Format / Design slides - NEED ASAP!!!

Format ONLY slides 4 - 11 and and slide 16.
Make look like slides 12 and 13.

Do NOT worry about slides after the Appendix.
Does not have to look super fancy, just better than what I have.

```html
<!DOCTYPE html>
<html lang="en">
<head>
<meta charset="utf-8">
<title>Investor Presentation – March 2026</title>
<link rel="stylesheet" href="https://fonts.googleapis.com/css2?family=Arimo:wght@400;700&display=swap">
<style>
:root{
  --blue:#1f6fb5;
  --navy:#1b2f7a;
  --green:#3a9e3a;
  --bar:#4aa83a;
  --light:#b9dc9f;
  --mid:#8fc97b;
  --teal:#4bacc6;
  --deep:#1f4e79;
  --sky:#00b0f0;
  --lime:#92d050;
  --ink:#222;
  --rule:#c9c9c9;
  --bg:#ececec;
}
*{box-sizing:border-box;margin:0;padding:0}
html,body{width:1200px;height:2727px;overflow:hidden;background:var(--bg);font-family:"Arimo",Arial,sans-serif;color:var(--ink)}
.slide{position:absolute;width:598px;height:434px;background:#fff;overflow:hidden}
.slide>*{position:absolute}
.col-l{left:0}.col-r{left:601px}
.title{left:12px;top:24px;font-size:11.5px;color:var(--blue);text-transform:uppercase;line-height:15px}
.title.big{text-transform:none;color:#222;font-size:17px;top:22px;left:12px}
.title-rule{left:10px;right:46px;top:46px;border-top:1px solid var(--rule)}
.brand{right:10px;top:12px;display:flex;align-items:center;gap:4px;font-weight:700;font-size:13px;color:var(--blue)}
.brand i{display:block;width:11px;height:11px;border-radius:50%;background:var(--blue)}
.footer{left:0;right:0;bottom:0;height:14px;background:var(--navy);color:#fff;font-size:5.5px;line-height:14px}
.footer span{position:absolute}
.footer .deck{left:20px}.footer .date{left:497px}
.footer .num{right:0;width:24px;height:14px;background:#fff;color:#777;text-align:center}
.hl{background:#ffff00;color:var(--blue)}
.item h3{font-size:10px;font-weight:400;color:var(--green);line-height:12px;margin-bottom:10px}
.item p{font-size:8px;line-height:10.5px;color:#333}
.icon{width:30px;height:30px}
.rule{border-top:1.5px solid var(--blue)}
.grule{border-top:1px solid var(--blue)}
.vrule{border-left:1.5px solid var(--blue)}
ul.dash{list-style:none;font-size:12px;line-height:15.5px}
ul.dash li{padding-left:18px;position:relative}
ul.dash li::before{content:"-";position:absolute;left:2px}
ul.dot{list-style:none;font-size:10.5px;line-height:14px;color:#333}
ul.dot li{padding-left:12px;position:relative}
ul.dot li::before{content:"•";position:absolute;left:2px}
.qh{font-size:13.5px;color:var(--blue);text-align:center}
.sec h2{font-size:12.5px;font-weight:400;color:var(--green);margin-bottom:8px}
.chart-cap{font-size:9.5px;color:#555;text-align:center}
.src{font-size:6.5px;color:#333;line-height:8px}
.quote-mark{font-size:54px;font-weight:700;color:var(--green);line-height:40px;letter-spacing:-6px}
.quote{font-size:11px;line-height:17px;color:#333}
.sig{font-size:11px;line-height:14px}
.sig b{font-weight:700;color:#222}.sig span{color:var(--green);display:block}
.stat b{display:block;font-weight:400;font-size:14px;color:var(--green);line-height:16px}
.stat p{font-size:9.5px;line-height:11px;color:#444}
.mini h4{font-size:10px;font-weight:400;color:var(--green);line-height:12px}
.mini ul{list-style:none;font-size:8px;line-height:11.5px;color:#333;margin-top:10px}
.mini li{padding-left:10px;position:relative}
.mini li::before{content:"•";position:absolute;left:1px}
.tiny{font-size:6px;color:#333}
svg{overflow:visible}
svg text{font-family:"Arimo",Arial,sans-serif}
table.guide{border-collapse:collapse;font-size:11px;color:#333}
table.guide th{font-weight:400;color:var(--blue);font-size:11px;padding:0 0 16px}
table.guide td{padding:12px 0 16px}
.assume{font-size:8.5px;line-height:11px;color:#333}
.assume h4{font-weight:400;color:var(--green);font-size:12px;margin-bottom:4px}
.assume li{list-style:none;padding-left:14px;position:relative}
.assume li::before{content:"-";position:absolute;left:0}
.graybox{background:#e8e8e8;border:1px solid #bbb;box-shadow:2px 2px 3px #aaa;text-align:center;font-size:18px;line-height:21px;padding-top:1px;color:#111}
.step{font-size:11px;color:#222;line-height:14px}
</style>
</head>
<body>

<section class="slide col-l" style="top:10px">
  <h1 class="title">Strong Growth at a Compelling Value</h1>
  <div class="brand"><i></i>MRC</div>
  <svg class="icon" style="left:40px;top:90px" viewBox="0 0 30 30" fill="none" stroke="var(--green)" stroke-width="1.4"><path d="M3 27h24M6 27v-6M11 27v-9M16 27v-7M21 27v-12M4 16l8-6 5 4 9-9M22 5h4v4"/></svg>
  <div class="item" style="left:78px;top:92px;width:150px"><h3>External Growth Strategy Off Small Asset Base:</h3><p>Since YE24 acquired ??? SHOP assets at low to mid teen IRRs. 2026 Guidance of 600M</p></div>
  <svg class="icon" style="left:332px;top:92px" viewBox="0 0 30 30" fill="none" stroke="var(--green)" stroke-width="1.4"><rect x="7" y="3" width="16" height="24" rx="1"/><path d="M11 9h8M11 13h8M11 17h8M11 21h5"/></svg>
  <div class="item" style="left:370px;top:100px;width:150px"><h3>Solid Balance Sheet:</h3><p>4.5x Debt to EBITDAre with $800 million credit facility providing significant liquidity</p></div>
  <div class="grule" style="left:28px;top:171px;width:258px"></div>
  <div class="grule" style="left:320px;top:171px;width:258px"></div>
  <svg class="icon" style="left:40px;top:206px" viewBox="0 0 30 30" fill="none" stroke="var(--green)" stroke-width="1.4"><circle cx="9" cy="15" r="5"/><circle cx="9" cy="15" r="1.5"/><path d="M16 9h11M16 15h9M16 21h11M24 6l3 3-3 3"/></svg>
  <div class="item" style="left:78px;top:208px;width:160px"><h3>Transformational Acceleration of Internal Growth:</h3><p>SHOP NOI To 40% of Portfolio By YE26 Transforming Annual Portfolio NOI Growth from 2.5% YE 24 to 5%+</p></div>
  <svg class="icon" style="left:332px;top:204px" viewBox="0 0 30 30" fill="none" stroke="var(--green)" stroke-width="1.4"><circle cx="7" cy="7" r="3"/><path d="M4 26h22M6 26v-5M11 26v-8M16 26v-6M21 26v-10M13 12l4-4 4 3 5-5"/></svg>
  <div class="item" style="left:370px;top:208px;width:150px"><h3>Strategy Benefits Not Fully Priced Into Shares:</h3><p>FAD multiple below peers</p></div>
  <div class="grule" style="left:28px;top:284px;width:258px"></div>
  <svg class="icon" style="left:38px;top:310px" viewBox="0 0 30 30" fill="none" stroke="var(--green)" stroke-width="1.4"><circle cx="13" cy="13" r="10"/><path d="M20 20l7 7M13 7l5 9H8z"/><path d="M13 11v2.5M13 14.8v.5"/></svg>
  <div class="item" style="left:78px;top:322px;width:175px"><h3>De-Risking:</h3><p>Reducing exposure to older skilled nursing assets, government reimbursement, individual tenant risks, and short-term loans</p></div>
  <footer class="footer"><span class="deck">INVESTOR PRESENTATION</span><span class="date">MARCH 2026</span><span class="num">4</span></footer>
</section>

<section class="slide col-r" style="top:10px">
  <h1 class="title">Recent Highlights (Q425 &amp; Q126)</h1>
  <div class="brand"><i></i>MRC</div>
  <div class="qh" style="left:24px;top:84px;width:260px">Q42025</div>
  <div class="rule" style="left:24px;top:104px;width:260px"></div>
  <ul class="dash" style="left:24px;top:118px;width:262px">
    <li>Acquired three SHOP communities for $84.2 million, with an expected unlevered IRR in the low teens.</li>
    <li>Converted two seniors housing communities in Oregon from our NNN into SHOP</li>
    <li>Sold seven skilled nursing centers for $123 million and recorded a total gain on sales of $78 million.</li>
    <li>Received cash proceeds of $8.2 million, inclusive of a 12% exit IRR of $1.8 million, from the redemption of a preferred equity investment in a joint venture.</li>
    <li>Received $16 million from the payoff of a mortgage loan secured by a seniors housing community.</li>
  </ul>
  <div class="rule" style="left:24px;top:372px;width:260px"></div>
  <div class="qh" style="left:300px;top:84px;width:262px">Q12026</div>
  <div class="rule" style="left:300px;top:104px;width:262px"></div>
  <ul class="dash" style="left:300px;top:118px;width:262px">
    <li>Acquired a seniors housing community within its SHOP segment for $108 million, with an expected unlevered IRR in the low teens.</li>
    <li>Converted two seniors housing communities in Texas from our NNN portfolio into SHOP.</li>
    <li>Sold $65 million SNF properties</li>
  </ul>
  <div class="rule" style="left:300px;top:372px;width:262px"></div>
  <footer class="footer"><span class="deck">INVESTOR PRESENTATION</span><span class="date">MARCH 2026</span><span class="num">5</span></footer>
</section>

<section class="slide col-l" style="top:465px">
  <h1 class="title" style="top:10px">Compelling Value<br>High SHOP Concentration Yet Amongst Lowest 2026 AFFO Multiple</h1>
  <div class="title-rule" style="top:40px"></div>
  <div class="brand"><i></i>MRC</div>
  <div class="chart-cap" style="left:30px;top:82px;width:240px">Proforma SHOP % of Total NOI Compare</div>
  <svg style="left:22px;top:100px" width="260" height="245" viewBox="0 0 260 245">
    <g font-size="6" fill="#555" text-anchor="end">
      <text x="24" y="235">0%</text><text x="24" y="210">10%</text><text x="24" y="185">20%</text><text x="24" y="160">30%</text><text x="24" y="134">40%</text><text x="24" y="109">50%</text><text x="24" y="84">60%</text><text x="24" y="59">70%</text><text x="24" y="34">80%</text><text x="24" y="8">90%</text>
    </g>
    <g stroke="#e4e4e4"><path d="M30 233h225M30 207h225M30 182h225M30 157h225M30 132h225M30 106h225M30 81h225M30 56h225M30 31h225M30 5h225"/></g>
    <g fill="var(--bar)">
      <rect x="37" y="39" width="16" height="194"/><rect x="64" y="52" width="16" height="181"/><rect x="91" y="100" width="16" height="133"/><rect x="118" y="132" width="16" height="101"/><rect x="145" y="160" width="16" height="73"/><rect x="172" y="183" width="16" height="50"/><rect x="199" y="230" width="16" height="3"/>
    </g>
    <g font-size="6" fill="#333" text-anchor="middle">
      <text x="42" y="36">77%</text><text x="72" y="49">72%</text><text x="99" y="97">53%</text><text x="126" y="129">40%</text><text x="153" y="157">29%</text><text x="180" y="180">20%</text><text x="207" y="226">1%</text><text x="234" y="230">0%</text>
    </g>
    <g font-size="5" fill="#333" text-anchor="middle">
      <text x="45" y="243">Peer B</text><text x="72" y="243">Peer A</text><text x="99" y="243">Peer C</text><text x="126" y="243">MRC</text><text x="153" y="243">Peer G</text><text x="180" y="243">Peer E</text><text x="207" y="243">Peer D</text><text x="234" y="243">Peer F</text>
    </g>
  </svg>
  <p class="src" style="left:28px;top:360px;width:240px">Source: Peer A, Peer E, MRC Proforma 2026 Per Earnings Calls / Business Update. All Others YE25</p>
  <div style="left:299px;top:88px;height:300px;border-left:1.5px solid var(--blue)"></div>
  <div class="chart-cap" style="left:320px;top:82px;width:240px">2626 AFFO Multiple</div>
  <svg style="left:316px;top:100px" width="260" height="245" viewBox="0 0 260 245">
    <g font-size="6" fill="#555" text-anchor="end">
      <text x="24" y="235">0.0x</text><text x="24" y="210">5.0x</text><text x="24" y="184">10.0x</text><text x="24" y="159">15.0x</text><text x="24" y="133">20.0x</text><text x="24" y="108">25.0x</text><text x="24" y="82">30.0x</text><text x="24" y="57">35.0x</text><text x="24" y="32">40.0x</text><text x="24" y="6">45.0x</text>
    </g>
    <g stroke="#e4e4e4"><path d="M30 233h225M30 207h225M30 182h225M30 156h225M30 131h225M30 105h225M30 80h225M30 54h225M30 29h225M30 4h225"/></g>
    <g fill="var(--bar)">
      <rect x="35" y="32" width="15" height="201"/><rect x="61" y="76" width="15" height="157"/><rect x="87" y="90" width="15" height="143"/><rect x="113" y="130" width="15" height="103"/><rect x="139" y="148" width="15" height="85"/><rect x="165" y="154" width="15" height="79"/><rect x="191" y="162" width="15" height="71"/><rect x="217" y="165" width="15" height="68"/>
    </g>
    <g font-size="6.5" fill="#333" text-anchor="middle">
      <text x="43" y="29">39.3x</text><text x="69" y="73">30.7x</text><text x="95" y="87">27.9x</text><text x="121" y="127">20.1x</text><text x="147" y="145">16.6x</text><text x="173" y="151">15.5x</text><text x="199" y="159">13.8x</text><text x="225" y="162">13.2x</text>
    </g>
    <g font-size="5" fill="#333" text-anchor="middle">
      <text x="43" y="243">Peer A</text><text x="69" y="243">Peer B</text><text x="95" y="243">Peer C</text><text x="121" y="243">Peer D</text><text x="147" y="243">Peer E</text><text x="173" y="243">Peer F</text><text x="199" y="243">MRC</text><text x="225" y="243">Peer G</text>
    </g>
  </svg>
  <p class="src" style="left:344px;top:362px">Source: Index Data Co, MRC Calculations</p>
  <footer class="footer"><span class="deck">INVESTOR PRESENTATION</span><span class="date">MARCH 2026</span><span class="num">6</span></footer>
</section>

<section class="slide col-r" style="top:465px">
  <h1 class="title big">Focused Portfolio Strategy To Enhance Shareholder Returns</h1>
  <div class="title-rule"></div>
  <div class="brand"><i></i>MRC</div>
  <svg class="icon" style="left:26px;top:60px" viewBox="0 0 30 30" fill="none" stroke="var(--green)" stroke-width="1.4"><path d="M3 27h24M6 27v-6M11 27v-9M16 27v-7M21 27v-12M4 16l8-6 5 4 9-9M22 5h4v4"/></svg>
  <div class="sec" style="left:65px;top:66px;width:500px"><h2>Increasing Internal Growth Through SHOP</h2>
    <ul class="dot"><li>Uniquely strong Seniors Housing fundamentals</li><li>Recycling short duration slow growth assets (10%-12% 5 Yr IRRs) into high growth long duration assets (15% +/- 5 Yr IRRs)</li></ul></div>
  <div class="grule" style="left:26px;top:152px;width:544px"></div>
  <svg class="icon" style="left:26px;top:164px" viewBox="0 0 30 30" fill="none" stroke="var(--green)" stroke-width="1.4"><circle cx="9" cy="15" r="5"/><circle cx="9" cy="15" r="1.5"/><path d="M16 9h11M16 15h9M16 21h11M24 6l3 3-3 3"/></svg>
  <div class="sec" style="left:65px;top:170px;width:500px"><h2>Accelerating External Growth</h2>
    <ul class="dot"><li>Opportunistically acquiring Seniors Housing &nbsp;assets at IRRs above WACC and below replacement cost</li><li>Acquired $565million SHOP YTD</li><li>5 Yr underwritten IRRs are expected to be in the low teens</li><li>2026 Guidance Midpoint ??? At 15% +/- IRRs</li></ul></div>
  <div class="grule" style="left:26px;top:290px;width:544px"></div>
  <svg class="icon" style="left:26px;top:298px" viewBox="0 0 30 30" fill="none" stroke="var(--green)" stroke-width="1.4"><path d="M6 3v20M2 19l4 5 4-5M15 3v20M11 19l4 5 4-5M24 3v20M20 19l4 5 4-5"/></svg>
  <div class="sec" style="left:65px;top:308px;width:500px"><h2>Reducing Portfolio Risk</h2>
    <ul class="dot"><li>Actively reducing SNF exposure</li><li>Increasing tenant / operator diversification</li><li>Reducing reinvestment risk from purchase options / loan repayments</li><li>Reducing average age of portfolio, improving asset quality and long-term performance</li></ul></div>
  <footer class="footer"><span class="deck">INVESTOR PRESENTATION</span><span class="date">MARCH 2026</span><span class="num">7</span></footer>
</section>

<section class="slide col-l" style="top:918px">
  <h1 class="title" style="top:26px">Solid Balance Sheet</h1>
  <div class="title-rule"></div>
  <div class="brand"><i></i>MRC</div>
  <svg style="left:24px;top:100px" width="40" height="40" viewBox="0 0 30 30" fill="none" stroke="var(--green)" stroke-width="1.3"><circle cx="15" cy="9" r="6"/><path d="M15 5v8M13 7h3.5a1.5 1.5 0 010 3H13"/><path d="M2 22c5-3 8-4 13 0h9l4-4M8 20l-3-5M22 20l3-5"/></svg>
  <div style="left:72px;top:108px;font-size:17px;color:var(--green)">Liquidity: $542.0 million*</div>
  <ul class="dash" style="left:72px;top:136px;width:210px;font-size:12px;line-height:16.5px">
    <li>$16 million cash on hand.</li>
    <li>$240 million available under the Company’s unsecured revolving line of credit with $360 million outstanding.</li>
    <li>$286 million available under the Company’s ATM</li>
  </ul>
  <div class="vrule" style="left:299px;top:86px;height:300px"></div>
  <svg style="left:328px;top:100px" width="30" height="40" viewBox="0 0 22 30" fill="none" stroke="var(--green)" stroke-width="1.2"><path d="M2 2h12l6 6v20H2z"/><path d="M14 2v6h6M6 14h10M6 18h10M6 22h10"/><text x="4" y="11" font-size="7" fill="var(--green)" stroke="none">$</text></svg>
  <div style="left:374px;top:108px;font-size:17px;color:var(--green)">*Proforma</div>
  <ul class="dash" style="left:374px;top:136px;width:200px"><li>Lorem Ipsum</li></ul>
  <footer class="footer"><span class="deck">INVESTOR PRESENTATION</span><span class="date">MARCH 2026</span><span class="num">8</span></footer>
</section>

<section class="slide col-r" style="top:918px">
  <h1 class="title" style="top:26px">Guidance <span class="hl">MAYBE NOT HERE</span></h1>
  <div class="title-rule"></div>
  <div class="brand"><i></i>MRC</div>
  <table class="guide" style="left:26px;top:82px;width:546px">
    <tr><th style="text-align:left;width:300px"></th><th style="text-align:center">Full year</th><th style="text-align:center">First Quarter</th></tr>
    <tr style="border-top:1.5px solid var(--blue)"><td style="padding-left:6px">Diluted earnings per common share</td><td style="text-align:center">$1.80 to $1.84</td><td style="text-align:center">$0.60 to $0.62</td></tr>
    <tr><td style="padding-left:6px">Diluted Core FFO per share</td><td style="text-align:center">2.75 to $2.79</td><td style="text-align:center">$0.66 to $0.68</td></tr>
    <tr style="border-bottom:1.5px solid var(--blue)"><td style="padding-left:6px">Diluted Core FAD per share</td><td style="text-align:center">$2.82 to $ 2.86</td><td style="text-align:center">$0.68 to $0.70</td></tr>
  </table>
  <div class="assume" style="left:26px;top:262px;width:546px"><h4>Assumptions:</h4>
    <ul>
      <li>Gross investments for the full year in the range of $400 million and $800 million, including transactions closed to date or expected to close over the next 60 days</li>
      <li>Asset sales and loan payoffs of $265.9 million for the 2026 full year and $73.5 million for Q12026</li>
      <li>SHOP NOI, inclusive of expected net investments, in the range of $65.1 million to $77 million for the full year, and $12 million to $13 million for Q12026</li>
      <li>&nbsp;SHOP FAD capital expenditures in the range of $4.6 million to $4.9 million for the full year, and $890,000 to $910,000 for Q12026</li>
      <li>G&amp;A &nbsp;costs for the full year in the range of $31.7 million to $33.9 million, and $8.4 million to $8.7 million for Q12026</li>
    </ul></div>
  <footer class="footer"><span class="deck">INVESTOR PRESENTATION</span><span class="date">MARCH 2026</span><span class="num">9</span></footer>
</section>

<section class="slide col-l" style="top:1373px">
  <div class="brand"><i></i>MRC</div>
  <div class="quote-mark" style="left:22px;top:88px">”</div>
  <div class="grule" style="left:22px;top:132px;width:258px"></div>
  <p class="quote" style="left:24px;top:140px;width:258px">“Our strategic shift toward SHOP is delivering higher growth and fundamentally reshaping our long-term earnings profile. With a more resilient portfolio consisting of newer assets and a focused approach to capital allocation, we ended 2025 with momentum and confidence in our ability to continue creating long-term value for shareholders.”</p>
  <div class="grule" style="left:22px;top:294px;width:163px"></div>
  <div class="sig" style="left:200px;top:287px"><b>Dana Whitfield</b><span>Co-CEO</span></div>
  <div class="quote-mark" style="left:308px;top:88px">”</div>
  <div class="grule" style="left:308px;top:132px;width:260px"></div>
  <p class="quote" style="left:312px;top:140px;width:262px">“The transformation of our portfolio to a material composition of higher-growth SHOP investments will drive better risk adjusted returns of our shareholders. We are executing on our SHOP strategy with speed, determination and conviction, with a goal of SHOP representing 45% of our investment portfolio by the end of 2026 to further enhance our growth profile.”</p>
  <div class="grule" style="left:322px;top:294px;width:163px"></div>
  <div class="sig" style="left:499px;top:287px"><b>Marcus Hale</b><span>Co-CEO</span></div>
  <footer class="footer"><span class="deck">INVESTOR PRESENTATION</span><span class="date">MARCH 2026</span><span class="num">10</span></footer>
</section>

<section class="slide col-r" style="top:1373px">
  <h1 class="title" style="top:26px">SHOP Spotlight</h1>
  <div class="title-rule"></div>
  <div class="brand"><i></i>MRC</div>
  <div class="stat" style="left:30px;top:80px"><b>9 years</b><p>Average Age</p></div>
  <div class="stat" style="left:167px;top:80px;width:122px"><b>$468 Million</b><p>SHOP Acquisitions Since May 2025</p></div>
  <div class="stat" style="left:303px;top:80px;width:124px"><b>22% NOI Growth</b><p>over 2024 proforma NOI for the original 13 property SHOP conversions</p></div>
  <div class="stat" style="left:441px;top:80px;width:130px"><b>14%</b><p>Projected 2026 Growth*</p></div>
  <div class="grule" style="left:26px;top:152px;width:548px"></div>
  <div class="stat" style="left:30px;top:165px"><b>7 Operators</b><p>5 New to MRC</p></div>
  <div class="stat" style="left:167px;top:165px"><b>X Units</b><p>……</p></div>
  <div class="stat" style="left:303px;top:165px;width:124px"><b>27%</b><p>SHOP as a % of Gross Investments<br>Up from 0% in May 2025</p></div>
  <div class="vrule" style="left:157px;top:76px;height:160px;border-left-width:1px"></div>
  <div class="vrule" style="left:293px;top:76px;height:160px;border-left-width:1px"></div>
  <div class="vrule" style="left:431px;top:76px;height:160px;border-left-width:1px"></div>
  <div class="quote-mark" style="left:22px;top:258px">”</div>
  <div class="grule" style="left:58px;top:272px;width:514px"></div>
  <p class="quote" style="left:28px;top:300px;width:548px;font-size:13.5px;line-height:18px;color:#222">“With SHOP now comprising 27% of our real estate portfolio and a robust pipeline in front of us, we’re positioned to scale quickly and convert that momentum into sustained NOI growth by continuing to add newer, high-quality assets.”</p>
  <footer class="footer"><span class="deck">INVESTOR PRESENTATION</span><span class="date">MARCH 2026</span><span class="num">11</span></footer>
</section>

<section class="slide col-l" style="top:1827px">
  <h1 class="title" style="top:24px;left:10px">Seniors Housing Operating Portfolio (“SHOP”) Transformation</h1>
  <div class="title-rule" style="top:44px"></div>
  <div class="brand"><i></i>MRC</div>
  <div class="mini" style="left:26px;top:58px;width:250px"><h4>2025 SHOP ACTIVITIES SINCE MAY ($565M)</h4>
    <ul><li>$353M in SHOP acquisitions</li><li>$212M - Three SHOP conversions</li><li>Seven SHOP operators, five new to MRC</li></ul></div>
  <div class="grule" style="left:14px;top:145px;width:258px"></div>
  <div class="mini" style="left:26px;top:163px;width:250px"><h4>2026 SHOP CONVERSIONS ($58M)</h4>
    <ul><li>$26M completed in 1Q26</li><li>$32M expected over the next 60 days</li><li>Two SHOP operators new to MRC</li></ul></div>
  <div class="mini" style="left:300px;top:62px;width:280px;text-align:center"><h4>SHOP GROWTH</h4><div class="tiny" style="font-size:4.5px">(DOLLAR AMOUNTS IN MILLIONS)</div></div>
  <svg style="left:296px;top:78px" width="290" height="150" viewBox="0 0 290 150">
    <g font-size="7" fill="#555" text-anchor="end"><text x="35" y="128">$0</text><text x="35" y="112">$200</text><text x="35" y="96">$400</text><text x="35" y="80">$600</text><text x="35" y="64">$800</text><text x="35" y="48">$1,000</text><text x="35" y="32">$1,200</text><text x="35" y="16">$1,400</text></g>
    <text x="6" y="80" font-size="4" fill="#555" transform="rotate(-90 6 80)" text-anchor="middle">GROSS ASSET VALUE</text>
    <rect x="143" y="79" width="40" height="47" fill="var(--light)" stroke="var(--bar)" stroke-width="1.5"/>
    <rect x="223" y="26" width="40" height="100" fill="var(--light)" stroke="var(--bar)" stroke-width="1.5"/>
    <text x="243" y="48" font-size="9" fill="var(--blue)" text-anchor="middle">116%</text>
    <path d="M40 126h240" stroke="#999"/>
    <path d="M72 122L240 12" stroke="#e21c1c" stroke-width="2.2"/><path d="M244 9l-9 2 5 6z" fill="#e21c1c"/>
    <g font-size="7" fill="#555" text-anchor="middle"><text x="80" y="136">2024</text><text x="163" y="136">2025</text><text x="243" y="136">Proforma 2026</text></g>
    <text x="148" y="148" font-size="5" fill="#333" text-anchor="middle">Proforma 2026 assumes $600M in SHOP investments (mid-point) and $58 M in SHOP conversions</text>
  </svg>
  <div class="grule" style="left:14px;top:252px;width:560px"></div>
  <div class="vrule" style="left:303px;top:258px;height:150px;border-left-width:1px"></div>
  <div class="mini" style="left:26px;top:268px;width:250px"><h4>2026 SHOP INVESTMENT GUIDANCE AND ACQUISITIONS COMPLETED TO DATE (~$400M - $800M)</h4>
    <ul><li>$108M SHOP acquisitions completed in 1Q26</li><li>$157M SHOP acquisitions over the next 60 days</li><li>$135M - $535M SHOP acquisitions expected to close through the end of 2026</li></ul></div>
  <div class="mini" style="left:334px;top:268px;width:240px"><h4>2026 INVESTMENT FUNDING STRATEGY</h4>
    <ul><li>~ $266M proceeds from SNF sales and loan prepayments</li><li>Proceeds from untapped opportunities within our portfolio, borrowings under our revolving line of credit, and sales under our ATM</li></ul></div>
  <footer class="footer"><span class="deck">INVESTOR PRESENTATION</span><span class="date">MARCH 2026</span><span class="num">12</span></footer>
</section>

<section class="slide col-r" style="top:1827px">
  <h1 class="title" style="top:22px;left:10px">Portfolio Transformation: Decreasing SNF and Loan Exposure</h1>
  <div class="tiny" style="left:10px;top:37px;font-size:4.3px">(PROFORMA 2026 ASSUMES $600M IN SHOP INVESTMENTS (MID-POINT) AND $58M IN SHOP CONVERSIONS)</div>
  <div class="title-rule" style="top:44px"></div>
  <div class="brand"><i></i>MRC</div>
  <div class="mini" style="left:28px;top:54px;width:262px"><h4 style="font-size:7.5px">ASSET TYPE TRANSFORMATION: 2024 - PROFORMA 2026</h4>
    <ul style="margin-top:3px;font-size:7px;line-height:10px"><li>Seniors Housing asset value concentration increases to 77%</li><li>Skilled Nursing asset value concentration decreases to 22%</li></ul></div>
  <div class="vrule" style="left:296px;top:54px;height:366px;border-left-width:1px"></div>
  <div class="mini" style="left:312px;top:54px;width:280px"><h4 style="font-size:7.5px">INVESTMENT TYPE TRANSFORMATION: 2024 - PROFORMA 2026</h4>
    <ul style="margin-top:3px;font-size:7px;line-height:10px"><li>Owned investments asset value concentration increases to 91%</li><li>Mortgage Loans investment asset value concentration decreases to 8%</li></ul></div>
  <div class="grule" style="left:10px;top:96px;width:578px"></div>
  <div class="mini" style="left:28px;top:104px"><h4 style="font-size:7.5px">2026 PROFORMA GROSS ASSET VALUE BY ASSET TYPE</h4></div>
  <svg style="left:10px;top:118px" width="280" height="130" viewBox="0 0 280 130">
    <g font-size="6" fill="#555" text-anchor="end"><text x="18" y="112">0%</text><text x="18" y="92">20%</text><text x="18" y="72">40%</text><text x="18" y="52">60%</text><text x="18" y="32">80%</text><text x="18" y="12">100%</text></g>
    <g stroke="#eee"><path d="M22 110h250M22 90h250M22 70h250M22 50h250M22 30h250M22 10h250"/></g>
    <rect x="42" y="10" width="44" height="54" fill="var(--bar)"/><rect x="42" y="64" width="44" height="46" fill="var(--teal)"/>
    <rect x="122" y="10" width="44" height="24" fill="var(--light)"/><rect x="122" y="34" width="44" height="39" fill="var(--bar)"/><rect x="122" y="73" width="44" height="36" fill="var(--teal)"/><rect x="122" y="109" width="44" height="1" fill="var(--deep)"/>
    <rect x="202" y="10" width="44" height="45" fill="var(--light)"/><rect x="202" y="55" width="44" height="32" fill="var(--bar)"/><rect x="202" y="87" width="44" height="22" fill="var(--teal)"/><rect x="202" y="109" width="44" height="1" fill="var(--deep)"/>
    <g font-size="5.5" fill="#222" text-anchor="middle"><text x="64" y="36">NNN</text><text x="64" y="42">54%</text><text x="64" y="86">SNF</text><text x="64" y="92">46%</text><text x="144" y="19">SHOP</text><text x="144" y="25">24%</text><text x="144" y="52">NNN</text><text x="144" y="58">39%</text><text x="144" y="90">SNF</text><text x="144" y="96">36%</text><text x="224" y="30">SHOP</text><text x="224" y="36">45%</text><text x="224" y="70">NNN</text><text x="224" y="76">32%</text><text x="224" y="97">SNF</text><text x="224" y="103">22%</text><text x="172" y="108">1%</text><text x="252" y="108">1%</text></g>
    <g font-size="6" fill="#444" text-anchor="middle"><text x="64" y="122">2024</text><text x="144" y="122">2025</text><text x="224" y="122">2026E</text></g>
  </svg>
  <div class="mini" style="left:312px;top:104px"><h4 style="font-size:7.5px">2026 PROFORMA GROSS ASSET VALUE BY INVESTMENT TYPE</h4></div>
  <svg style="left:302px;top:118px" width="290" height="130" viewBox="0 0 290 130">
    <g font-size="6" fill="#555" text-anchor="end"><text x="22" y="112">0%</text><text x="22" y="92">20%</text><text x="22" y="72">40%</text><text x="22" y="52">60%</text><text x="22" y="32">80%</text><text x="22" y="12">100%</text></g>
    <g stroke="#eee"><path d="M26 110h255M26 90h255M26 70h255M26 50h255M26 30h255M26 10h255"/></g>
    <rect x="48" y="10" width="44" height="64" fill="var(--bar)"/><rect x="48" y="74" width="44" height="17" fill="var(--mid)"/><rect x="48" y="91" width="44" height="15" fill="var(--teal)"/><rect x="48" y="106" width="44" height="4" fill="var(--deep)"/>
    <rect x="128" y="10" width="44" height="24" fill="var(--light)"/><rect x="128" y="34" width="44" height="44" fill="var(--bar)"/><rect x="128" y="78" width="44" height="15" fill="var(--mid)"/><rect x="128" y="93" width="44" height="16" fill="var(--teal)"/><rect x="128" y="109" width="44" height="1" fill="var(--deep)"/>
    <rect x="208" y="10" width="44" height="45" fill="var(--light)"/><rect x="208" y="55" width="44" height="36" fill="var(--bar)"/><rect x="208" y="91" width="44" height="10" fill="var(--mid)"/><rect x="208" y="101" width="44" height="8" fill="var(--teal)"/><rect x="208" y="109" width="44" height="1" fill="var(--deep)"/>
    <g font-size="5" fill="#222" text-anchor="middle"><text x="70" y="40">NNN</text><text x="70" y="46">64%</text><text x="70" y="84">Fin Rec, 17%</text><text x="70" y="100">Mortg Loans, 15%</text><text x="100" y="108">4%</text><text x="150" y="20">SHOP</text><text x="150" y="26">24%</text><text x="150" y="54">NNN</text><text x="150" y="60">44%</text><text x="150" y="87">Fin Rec, 15%</text><text x="150" y="103">Mortg Loans, 16%</text><text x="230" y="30">SHOP</text><text x="230" y="36">45%</text><text x="230" y="71">NNN</text><text x="230" y="77">36%</text><text x="230" y="97">Fin Rec, 10%</text><text x="230" y="106">Mortg Loans, 8%</text><text x="258" y="108">1%</text></g>
    <g font-size="6" fill="#444" text-anchor="middle"><text x="70" y="122">2024</text><text x="150" y="122">2025</text><text x="230" y="122">2026E</text></g>
  </svg>
  <div class="grule" style="left:10px;top:264px;width:578px"></div>
  <div class="mini" style="left:28px;top:286px"><h4 style="font-size:7.5px">2026 PROFORMA NOI BY ASSET TYPE</h4></div>
  <svg style="left:28px;top:310px" width="120" height="60" viewBox="0 0 120 60" font-size="4.5" fill="#333">
    <rect x="0" y="3" width="7" height="7" fill="var(--bar)"/><text x="11" y="9">SENIORS HOUSING - NNN</text>
    <rect x="0" y="17" width="7" height="7" fill="var(--light)"/><text x="11" y="23">SENIORS HOUSING - SHOP</text>
    <rect x="0" y="31" width="7" height="7" fill="var(--teal)"/><text x="11" y="37">SKILLED NURSING</text>
    <rect x="0" y="45" width="7" height="7" fill="var(--deep)"/><text x="11" y="51">OTHER/UDP</text>
  </svg>
  <svg style="left:160px;top:302px" width="110" height="110" viewBox="-21 -21 42 42" role="img" aria-label="Pie chart of 2026 proforma NOI by asset type">
    <g transform="rotate(-90)" fill="none" stroke-width="16">
      <circle r="8" stroke="var(--teal)" stroke-dasharray="14.07 50.27"/>
      <circle r="8" stroke="var(--deep)" stroke-dasharray="0.5 50.27" stroke-dashoffset="-14.07"/>
      <circle r="8" stroke="var(--bar)" stroke-dasharray="15.58 50.27" stroke-dashoffset="-14.57"/>
      <circle r="8" stroke="var(--light)" stroke-dasharray="20.11 50.27" stroke-dashoffset="-30.16"/>
    </g>
    <g font-size="3.6" fill="#222" text-anchor="middle"><text x="7" y="-6">28%</text><text x="5" y="10">31%</text><text x="-9" y="2">40%</text><text x="19" y="-1">1%</text></g>
  </svg>
  <div class="mini" style="left:312px;top:286px"><h4 style="font-size:7.5px">2026 PROFORMA NOI BY INVESTMENT TYPE</h4></div>
  <svg style="left:312px;top:310px" width="120" height="74" viewBox="0 0 120 74" font-size="4.3" fill="#333">
    <rect x="0" y="2" width="7" height="7" fill="var(--bar)"/><text x="11" y="8">OWNED PORTFOLIO - NNN</text>
    <rect x="0" y="15" width="7" height="7" fill="var(--light)"/><text x="11" y="21">OWNED PORTFOLIO - SHOP</text>
    <rect x="0" y="28" width="7" height="7" fill="var(--mid)"/><text x="11" y="32">OWNED ACCOUNTED</text><text x="11" y="37">FOR AS FINANCING RECEIVABLES</text>
    <rect x="0" y="46" width="7" height="7" fill="var(--teal)"/><text x="11" y="52">MORTGAGE LOANS</text>
    <rect x="0" y="59" width="7" height="7" fill="var(--deep)"/><text x="11" y="65">NOTES REC &amp; UNCONS JV</text>
  </svg>
  <svg style="left:462px;top:302px" width="110" height="110" viewBox="-21 -21 42 42" role="img" aria-label="Pie chart of 2026 proforma NOI by investment type">
    <g transform="rotate(-90)" fill="none" stroke-width="16">
      <circle r="8" stroke="var(--teal)" stroke-dasharray="4.02 50.27"/>
      <circle r="8" stroke="var(--deep)" stroke-dasharray="1.01 50.27" stroke-dashoffset="-4.02"/>
      <circle r="8" stroke="var(--bar)" stroke-dasharray="20.11 50.27" stroke-dashoffset="-5.03"/>
      <circle r="8" stroke="var(--light)" stroke-dasharray="20.11 50.27" stroke-dashoffset="-25.14"/>
      <circle r="8" stroke="var(--mid)" stroke-dasharray="5.02 50.27" stroke-dashoffset="-45.25"/>
    </g>
    <g font-size="3.6" fill="#222" text-anchor="middle"><text x="8" y="6">40%</text><text x="-9" y="2">40%</text><text x="-3" y="-10">10%</text><text x="6" y="-18">8%</text><text x="18" y="-9">2%</text></g>
  </svg>
  <footer class="footer"><span class="deck">INVESTOR PRESENTATION</span><span class="date">MARCH 2026</span><span class="num">13</span></footer>
</section>

<section class="slide col-l" style="top:2282px">
  <div class="brand"><i></i>MRC</div>
  <div class="graybox" style="left:40px;top:58px;width:524px;height:44px">Portfolio Recycling + SHOP Acquisitions =<br>Powerful Driver of Earnings &amp; Value Creation</div>
  <svg style="left:36px;top:106px" width="196" height="120" viewBox="0 0 196 120">
    <rect x=".5" y=".5" width="195" height="119" fill="#fff" stroke="#ddd"/>
    <text x="98" y="10" font-size="6" fill="#555" text-anchor="middle">Expected 5 Year IRRs Dispo / Loan Payoffs</text>
    <g stroke="#eee"><path d="M18 100h172M18 86h172M18 72h172M18 58h172M18 44h172M18 30h172"/></g>
    <rect x="32" y="51" width="18" height="49" fill="var(--deep)"/><rect x="76" y="90" width="18" height="10" fill="var(--lime)"/><rect x="120" y="99" width="18" height="1" fill="#ccc"/><rect x="164" y="27" width="18" height="73" fill="var(--sky)"/>
    <g font-size="3.6" fill="#555" text-anchor="middle"><text x="41" y="48">10%</text><text x="85" y="87">2%</text><text x="129" y="96">0%</text><text x="173" y="24">15%</text><text x="41" y="107">Dispo / Loans</text><text x="85" y="107">Excess Cash</text><text x="129" y="107">Capex</text><text x="173" y="107">SHOP IRR</text></g>
  </svg>
  <div class="chart-cap" style="left:56px;top:232px;width:160px;color:#333;font-size:9.5px">WACC - 70%/30% Debt / Equity Split</div>
  <svg style="left:40px;top:258px" width="190" height="100" viewBox="0 0 190 100">
    <g font-size="6" fill="#555" text-anchor="end"><text x="28" y="82">0.00%</text><text x="28" y="70">2.00%</text><text x="28" y="58">4.00%</text><text x="28" y="46">6.00%</text><text x="28" y="34">8.00%</text><text x="28" y="22">10.00%</text></g>
    <rect x="50" y="32" width="16" height="48" fill="var(--teal)"/><rect x="102" y="50" width="16" height="30" fill="var(--lime)"/><rect x="154" y="37" width="16" height="43" fill="var(--sky)"/>
    <g font-size="6" fill="#333" text-anchor="middle"><text x="58" y="29">8.00%</text><text x="110" y="47">5.00%</text><text x="162" y="34">7.10%</text><text x="58" y="90" font-size="5">Equity</text><text x="110" y="90" font-size="5">Debt</text><text x="162" y="90" font-size="5">WACC</text></g>
  </svg>
  <svg style="left:280px;top:134px" width="60" height="44" viewBox="0 0 60 44"><path d="M2 12h32V2l24 20-24 20V32H2z" fill="var(--teal)" stroke="#2b7f99" stroke-width="1.5"/></svg>
  <div class="step" style="left:360px;top:148px;width:180px">SHOP 500 BP Spread To Dispo IRR</div>
  <div class="chart-cap" style="left:376px;top:186px;width:140px;color:#444;font-size:9.5px">Expected After Capex 5 Year IRRs SHOP</div>
  <svg style="left:356px;top:212px" width="180" height="80" viewBox="0 0 180 80">
    <g font-size="5.5" fill="#555" text-anchor="end"><text x="14" y="8">20%</text><text x="14" y="18">15%</text><text x="14" y="28">10%</text><text x="14" y="38">5%</text><text x="14" y="48">0%</text><text x="14" y="58">-5%</text></g>
    <path d="M18 46h160" stroke="#bbb" stroke-width=".6"/>
    <rect x="26" y="32" width="10" height="14" fill="var(--teal)"/><rect x="48" y="26" width="10" height="20" fill="var(--lime)"/><rect x="70" y="46" width="10" height="2" fill="#e21c1c"/><rect x="94" y="46" width="10" height="1" fill="#ddd"/><rect x="148" y="14" width="10" height="32" fill="var(--sky)"/>
    <g font-size="5.5" fill="#333" text-anchor="middle"><text x="31" y="29">7%</text><text x="53" y="23">10%</text><text x="75" y="56">-1%</text><text x="99" y="55">-0.25%</text><text x="153" y="11">15.8%</text></g>
    <g font-size="4.5" fill="#555" text-anchor="middle"><text x="31" y="64">Initial</text><text x="31" y="70">RIDEA</text><text x="31" y="76">Yield</text><text x="53" y="64">NOI</text><text x="53" y="70">Growth</text><text x="75" y="64">Capex</text><text x="99" y="64">RIDEA Tax</text><text x="99" y="70">Leakage</text><text x="153" y="64">Total IRR</text></g>
  </svg>
  <svg style="left:280px;top:300px" width="60" height="44" viewBox="0 0 60 44"><path d="M2 12h32V2l24 20-24 20V32H2z" fill="var(--teal)" stroke="#2b7f99" stroke-width="1.5"/></svg>
  <div class="step" style="left:360px;top:316px;width:180px">SHOP 700 BP Spread To WACC</div>
  <div style="right:14px;bottom:10px;font-size:6px;color:#777">14</div>
</section>

</body>
</html>
```